Poster to promote Global Critter Care Fest

Hi Designers,

Animal lovers all over the world are grateful for the work of vets.

To recognize all their efforts, Global Critter Care Fest takes place globally on April 30. This year's theme is 'Continuing education with a one health focus'.

It's about working alongside the human health sector to tackle animal disease and food safety. Read more here: http://www.brenvalu.org/for-the-media/press-releases/detail/article/global-critter-care-fest-award-2016/

We want you to design a poster to promote the day, and the key message.

The poster must feature:
- the words 'Global Critter Care Fest'
- the date 'April 30, 2016'
- the theme 'Continuing education with a one health focus

You can choose any imagery and colors you feel will be engaging for the audience and will reflect the industry and messages.

Think animal, vets, pets, caring, health.

Looking forward to seeing your ideas.

Thanks

PixelHive

• - the words 'Global Critter Care Fest'
• - the date 'April 30, 2016'
• - the theme 'Continuing education with a one health focus

```html
<!DOCTYPE html>
<html lang="en">
<head>
<meta charset="utf-8">
<title>Global Critter Care Fest – Poster</title>
<link href="https://fonts.googleapis.com/css2?family=Arimo:wght@400;700&display=swap" rel="stylesheet">
<style>
  :root {
    --stage: #151515;
    --sky-blue: #00aeef;
    --bar-blue: #1ba3e0;
    --paper: #ffffff;
    --photo-light: #f7f5f2;
    --photo-warm: #c89a5e;
    --photo-coat: #eef1f4;
    --partner-green: #8a8f2a;
    --partner-teal: #8fb8c4;
    --partner-red: #9b1b3a;
    --ink-grey: #4a4a4a;
  }
  * { margin: 0; padding: 0; box-sizing: border-box; }
  html, body { width: 1200px; height: 1200px; overflow: hidden; }
  body {
    background: var(--stage);
    font-family: "Arimo", Arial, sans-serif;
    display: flex; align-items: center; justify-content: center;
  }
  .poster {
    position: relative;
    width: 781px; height: 1108px;
    background: var(--paper);
    overflow: hidden;
  }
  .top-bar { position: absolute; top: 0; left: 0; right: 0; height: 15px; background: var(--bar-blue); }
  .event-title {
    position: absolute; top: 58px; left: 0; right: 0;
    text-align: center; color: var(--sky-blue);
    font-weight: 700; font-size: 45px; letter-spacing: 0.3px;
  }
  .event-date {
    position: absolute; top: 114px; left: 0; right: 0;
    text-align: center; color: var(--sky-blue);
    font-weight: 700; font-size: 28px;
  }
  .event-date sup { font-size: 15px; }
  .hero-photo {
    position: absolute; top: 160px; left: 0; right: 0; height: 540px;
    background:
      radial-gradient(ellipse 38% 55% at 28% 70%, var(--photo-warm) 0%, rgba(200,154,94,0.55) 55%, rgba(200,154,94,0) 100%),
      radial-gradient(ellipse 30% 60% at 72% 55%, var(--photo-coat) 0%, rgba(238,241,244,0) 100%),
      var(--photo-light);
  }
  .wave { position: absolute; top: 640px; left: 0; width: 781px; height: 60px; }
  .theme-band {
    position: absolute; top: 698px; left: 0; right: 0; height: 285px;
    background: var(--sky-blue);
  }
  .theme-text {
    position: absolute; top: 38px; left: 64px;
    color: var(--paper); font-size: 57px; line-height: 63px; font-weight: 400;
  }
  .theme-text strong { font-weight: 700; }
  .partners {
    position: absolute; top: 983px; left: 0; right: 0; bottom: 0;
    display: flex; align-items: center; gap: 34px; padding-left: 68px;
  }
  .partner { display: flex; align-items: center; gap: 8px; font-size: 13px; font-weight: 700; line-height: 15px; }
  .partner-guild { color: var(--partner-green); }
  .partner-badge { width: 82px; height: 82px; border-radius: 50%; background: var(--partner-teal); opacity: 0.6; }
  .partner-org { color: var(--partner-red); }
  .partner-mark { width: 18px; height: 18px; border-radius: 50%; background: currentColor; }
</style>
</head>
<body>
  <main class="poster">
    <div class="top-bar"></div>
    <h1 class="event-title">GLOBAL CRITTER CARE FEST</h1>
    <p class="event-date">April 30<sup>th</sup>, 2016</p>

    <div class="hero-photo" role="img" aria-label="Photo of a smiling vet in a white coat with a stethoscope, writing notes while a German Shepherd dog licks his cheek"></div>

    <svg class="wave" viewBox="0 0 781 60" preserveAspectRatio="none" aria-hidden="true">
      <path d="M0 40 L60 22 L280 24 L320 4 L460 32 L650 20 L781 40 L781 60 L0 60 Z" fill="var(--sky-blue)"/>
    </svg>

    <section class="theme-band">
      <p class="theme-text">Continuing<br>Education with a<br><strong>One Health Focus</strong></p>
    </section>

    <footer class="partners">
      <div class="partner partner-guild"><span class="partner-mark"></span><span>GLOBAL VET<br>GUILD</span></div>
      <div class="partner-badge" role="img" aria-label="Partner badge"></div>
      <div class="partner partner-org"><span>BRENVALU<br>ANIMAL CARE ORG</span></div>
    </footer>
  </main>
</body>
</html>
```